Famous Australian Web Brand (SiteKeyHub.com.au) Needs a New Website & Logo

SiteKeyHub.com.au is one of the leading domain name registration businesses in Australia and is looking for an overhaul of its website and brand.

SiteKeyHub.com.au current products/services include domain name registration, web hosting, web site creation and SSL certificates.

In this design contest on PixelSwarm, we would like designers to create a new logo and new website design for SiteKeyHub.com.au.

Here is what contest entrants will need to create:
- 1 new logo
- 1 new home page design
- 1 internal page (pricing page)

The winning designer will receive the main prize of $750. In addition to this, the winning designer will have the opportunity to work with SiteKeyHub for the build of the full website and may get ongoing design work from SiteKeyHub.
Updates

thank you all for your designs, we are after a web 2.0 look and feel, please dont use serif fonts, lets use modern and sleek ones, i will upload some samples of one we like shortly

header is to be in black with some texturing, white fonts and the call to action buttons are in green.

for the 6 free services, please use round edges for the images with the text under it, as i will upload shortly and we would like custome images, not stockimage types please

im uploading a sample of a background image for the header, which is black with texturing and also and image for the footer/middle of the page which has the correct shading of the grey for the middle section

please see file 8 for the look we are trying to get with our site and for font ideas

Reason: we have decided to extend the contest for another 3 days as a couple of designers have requested a bit more time

Target Market(s)

People that might need to buy a domain name or start a website: small business owners; entrepreneurs; bloggers; everyone from mum-and-dad website owners to tech savvy entrepreneurs. Geographically we will be targeting Australia but this should not influence the design.

Industry/Entity Type

Build

Requirements
Must have
• The logo should:
- Have the text "SiteKeyHub"
- Be positioned in the top left hand corner of the website
- Be either a wordmark, pictorial or abstract logo. That is, text-only logos are acceptable but we are also interested in receiving logos with a mark to the left that could somehow represents the business that we’re in

The homepage should:
- Feel modern, slick, web2.0
- Have a horizontal menu with 4 menu items: About Us | Contact Us | My Cart | Login
- Include the logo at the top
- Include the content from this Word Document
- Include the rough layout and style from this JPG template layout

The interior page should:
- Have the same look and feel as the home page
- Include the rough layout and style from this JPG attachment
- Include the content from this second Word Document
Nice to have
• - Grey, white and black primary colors
- Buttons that are green or lime green with a web2.0 call to action
- Full-width design (i.e. across the screen like PixelSwarm)
Should not have
• - Do not include overt Australian references. While we are an Australian business we do not want Australian flags, kangaroos or Captain Bellwether in our logo or on our website.
- Do not use the current red color scheme in the design. We want to move away from this.

```html
<!DOCTYPE html>
<html lang="en">
<head>
<meta charset="utf-8">
<title>SiteKeyHub – Domains, Hosting and Websites</title>
<link rel="stylesheet" href="https://fonts.googleapis.com/css2?family=Montserrat:wght@300;400;600&family=Arimo:wght@400;700&display=swap">
<style>
:root{
  --ink:#0b0b0b;
  --header-dark:#262626;
  --header-mid:#343434;
  --topbar:#1a1a1a;
  --green:#7cc242;
  --green-dark:#4f9a1f;
  --grey-band:#c9c9c9;
  --grey-light:#e4e4e4;
  --text:#3a3a3a;
  --heading:#111;
  --white:#fff;
  --footer-line:#3c3c3c;
  --footer-text:#d8d8d8;
  --footer-head:#a9a9a9;
}
*{box-sizing:border-box;margin:0;padding:0}
html,body{width:1029px;height:1200px;overflow:hidden;background:var(--white)}
body{position:relative;font-family:"Arimo",Arial,sans-serif;color:var(--text)}
a{color:inherit;text-decoration:none}

/* header */
.site-header{position:absolute;left:0;top:0;width:1029px;height:343px;
  background:radial-gradient(ellipse at 50% 35%,var(--header-mid) 0%,var(--header-dark) 60%,#1c1c1c 100%)}
.top-bar{height:30px;background:var(--topbar);border-bottom:1px solid #3a3a3a;display:flex;justify-content:flex-end;padding-right:102px}
.top-bar a{font-family:"Arimo",sans-serif;font-size:10.5px;color:#ddd;line-height:30px;padding:0 12px;border-left:1px solid #333}
.top-bar a:first-child{border-left:none}
.brand{position:absolute;left:118px;top:46px;display:flex;align-items:center;gap:10px}
.brand-dot{width:22px;height:22px;border-radius:50%;background:var(--green)}
.brand-name{font-family:"Montserrat",sans-serif;font-weight:400;font-size:27px;color:var(--white);letter-spacing:.3px}
.main-nav{position:absolute;right:85px;top:51px;display:flex;gap:27px}
.main-nav a{font-family:"Montserrat",sans-serif;font-size:12px;color:#c9c9c9;letter-spacing:.3px}
.main-nav a.is-active{color:var(--green)}
.nav-pointer{position:absolute;left:554px;top:30px;width:0;height:0;border-left:5px solid transparent;border-right:5px solid transparent;border-top:6px solid #000}
.headline{position:absolute;left:129px;top:106px;font-family:"Montserrat",sans-serif;font-weight:300;font-size:36px;line-height:41px;color:var(--white)}
.question{position:absolute;left:718px;top:130px;font-family:"Montserrat",sans-serif;font-weight:300}
.question p{font-size:23px;color:var(--white)}
.question .phone{display:flex;align-items:center;gap:6px;font-size:23px;color:var(--green);margin-top:2px}
.header-rule{position:absolute;left:110px;top:217px;width:823px;height:1px;background:#111;box-shadow:0 1px 0 #3d3d3d}
.domain-search{position:absolute;left:197px;top:236px;width:657px;height:53px;background:#0d0d0d;border-radius:4px;border:1px solid #3a3a3a;padding:9px 10px 0 12px;display:flex;gap:8px}
.domain-field{display:flex;width:611px;height:32px;background:var(--white);border:2px solid #999}
.domain-field .prefix{flex:1;font-family:"Arimo",sans-serif;font-weight:700;font-size:13px;color:#222;line-height:28px;padding-left:11px}
.domain-field .tld{width:71px;background:#e9e9e9;border-left:1px solid #bbb;font-weight:700;font-size:12px;color:#222;line-height:28px;padding-left:8px;display:flex;align-items:center;gap:9px}
.search-btn{width:117px;height:32px;border-radius:3px;background:linear-gradient(#9ed35e,var(--green) 50%,#5ca82a);border:1px solid #8dc653;color:var(--white);font-family:"Montserrat",sans-serif;font-weight:600;font-size:13px;letter-spacing:1px;text-align:center;line-height:30px}
.domain-links{position:absolute;left:0;top:307px;width:1029px;display:flex;justify-content:center;gap:47px;padding-left:10px}
.domain-links a{font-family:"Montserrat",sans-serif;font-size:13px;color:var(--white);letter-spacing:1px}

/* video band */
.video-band{position:absolute;left:0;top:343px;width:1029px;height:157px;background:var(--grey-band);border-top:1px solid #999}
.video-card{position:absolute;top:21px;width:258px;height:123px;background:var(--white);border:1px solid #aaa}
.video-card .still{position:absolute;right:0;top:0;width:130px;height:96px;background:linear-gradient(#f4f4f4,#ddd)}
.video-card .play{position:absolute;left:56px;top:34px}
.video-card .caption{position:absolute;left:0;bottom:0;width:100%;height:26px;background:#000;color:var(--white);font-family:"Montserrat",sans-serif;font-size:13px;line-height:26px;text-align:center}
.light-band{position:absolute;left:0;top:500px;width:1029px;height:29px;background:var(--grey-light)}

/* promo band */
.promo-band{position:absolute;left:0;top:529px;width:1029px;height:69px;background:#000;z-index:2;overflow:visible;
  text-align:center;font-family:"Montserrat",sans-serif;font-weight:300;color:var(--white);font-size:26px;line-height:31px;padding-top:2px}
.promo-band .line1{height:31px}
.promo-band .line2{height:31px;display:flex;justify-content:center;align-items:center;gap:14px;padding-left:58px}
.free-tag{display:inline-block;position:relative;top:10px;width:80px;height:36px;border-radius:6px;background:linear-gradient(#9ed35e,#5ca82a);
  font-weight:600;font-size:19px;line-height:36px;color:var(--white);transform:rotate(6deg)}

/* features */
.features{position:absolute;left:0;top:598px;width:1029px;height:421px;background:linear-gradient(#eeeeee 0,#fff 60px)}
.feature{position:absolute;width:258px}
.feature h3{display:flex;align-items:center;gap:6px;font-family:"Montserrat",sans-serif;font-weight:400;font-size:14px;color:var(--heading);height:20px}
.feature p{font-family:"Arimo",sans-serif;font-size:11px;line-height:20.6px;color:var(--text);margin-top:7px}

/* footer */
.site-footer{position:absolute;left:0;top:1019px;width:1029px;height:181px;background:#000;border-top:1px solid #333}
.footer-col{position:absolute;top:20px}
.footer-col h4{font-family:"Montserrat",sans-serif;font-weight:400;font-size:12px;color:var(--footer-head);padding:0 0 4px 1px;border-bottom:1px solid var(--footer-line)}
.footer-col li{list-style:none;font-size:10.5px;color:var(--footer-text);height:26px;line-height:26px;padding-left:5px;border-bottom:1px solid var(--footer-line)}
.footer-contact{position:absolute;left:734px;top:20px;font-family:"Montserrat",sans-serif;color:var(--white)}
.footer-contact .ask{font-size:13px;letter-spacing:.4px}
.footer-contact .big{font-size:26px;letter-spacing:4px;line-height:32px}
.footer-contact .phone{font-weight:300;font-size:23px;color:var(--green);margin-left:3px}
</style>
</head>
<body>

<header class="site-header">
  <nav class="top-bar" aria-label="Account">
    <a href="#">About Us</a><a href="#">Contact Us</a><a href="#">My Cart</a><a href="#">Login</a>
  </nav>
  <span class="nav-pointer"></span>
  <a class="brand" href="#"><span class="brand-dot"></span><span class="brand-name">SiteKeyHub</span></a>
  <nav class="main-nav" aria-label="Main">
    <a class="is-active" href="#">DOMAINS</a><a href="#">CREATOR</a><a href="#">EMAIL</a><a href="#">HOSTING</a><a href="#">MARKETING</a>
  </nav>
  <h1 class="headline">You get a lot more<br>than just a domain name.</h1>
  <div class="question">
    <p>Have a question?</p>
    <div class="phone">
      <svg width="24" height="22" viewBox="0 0 24 22"><path d="M4 2c2-1 3 0 4 2l1 3c0 1-1 2-2 2 1 3 3 5 6 6 0-1 1-2 2-2l3 1c2 1 2 2 1 4-1 2-3 3-6 2C7 18 3 13 2 8 1 5 2 3 4 2z" fill="#7cc242"/><path d="M15 3a6 6 0 0 1 5 5M15 6a3 3 0 0 1 2 2" stroke="#7cc242" stroke-width="1.4" fill="none"/></svg>
      <span>1300 55 01 27</span>
    </div>
  </div>
  <div class="header-rule"></div>
  <form class="domain-search">
    <div class="domain-field"><span class="prefix">www.</span><span class="tld">.COM <svg width="9" height="6" viewBox="0 0 9 6"><path d="M1 1l3.5 3.5L8 1" stroke="#222" stroke-width="2" fill="none"/></svg></span></div>
    <div class="search-btn">SEARCH</div>
  </form>
  <div class="domain-links"><a href="#">Renew a domain</a><a href="#">Transfer a domain</a><a href="#">View Price List</a></div>
</header>

<section class="video-band">
  <article class="video-card" style="left:123px">
    <div class="still" role="img" aria-label="Photo of a smiling woman in a dark top"></div>
    <svg class="play" width="30" height="30" viewBox="0 0 30 30"><circle cx="15" cy="15" r="14" fill="#eee" stroke="#bbb"/><path d="M11 8l11 7-11 7z" fill="#7cc242"/></svg>
    <div class="caption">Everyone needs a domain name</div>
  </article>
  <article class="video-card" style="left:402px">
    <div class="still" role="img" aria-label="Photo of a thoughtful young woman looking up"></div>
    <svg class="play" width="30" height="30" viewBox="0 0 30 30"><circle cx="15" cy="15" r="14" fill="#eee" stroke="#bbb"/><path d="M11 8l11 7-11 7z" fill="#7cc242"/></svg>
    <div class="caption">How you can use a domain name</div>
  </article>
  <article class="video-card" style="left:680px">
    <div class="still" role="img" aria-label="Photo of a woman giving two thumbs up"></div>
    <svg class="play" width="30" height="30" viewBox="0 0 30 30"><circle cx="15" cy="15" r="14" fill="#eee" stroke="#bbb"/><path d="M11 8l11 7-11 7z" fill="#7cc242"/></svg>
    <div class="caption">Why choose SiteKeyHub</div>
  </article>
</section>
<div class="light-band"></div>

<section class="promo-band">
  <div class="line1">Everything your business needs to be successful</div>
  <div class="line2"><span>online is</span><span class="free-tag">FREE</span><span>with every domain name.</span></div>
</section>

<section class="features">
  <article class="feature" style="left:123px;top:46px">
    <h3><svg width="16" height="18" viewBox="0 0 16 18"><rect x="4" y="1" width="10" height="13" fill="none" stroke="#5ca82a" stroke-width="1.6"/><rect x="1.5" y="4" width="10" height="13" fill="#fff" stroke="#5ca82a" stroke-width="1.6"/></svg>Free 15 Page Website</h3>
    <p>Create a professional, full-featured website in minutes without any technical knowledge. Choose from 4,000+ stunning website designs and customize your site with near-limitless options. Upload your own artwork for a truly personalised look.</p>
  </article>
  <article class="feature" style="left:402px;top:46px">
    <h3><svg width="24" height="18" viewBox="0 0 24 18"><path d="M2 7L12 1l10 6v10H2z" fill="#5ca82a"/><path d="M2 7l10 6 10-6" stroke="#fff" stroke-width="1.4" fill="none"/></svg>Free Professional Email</h3>
    <p>Having a personalised address that matches your domain name (for example, Sam@SamsBakery.com or Sales@SamsBakery.com) gives your company a much more professional image when you communicate with customers and associates.</p>
  </article>
  <article class="feature" style="left:680px;top:46px">
    <h3><svg width="14" height="18" viewBox="0 0 14 18"><rect x="1" y="0" width="11" height="18" fill="#5ca82a"/></svg>Free Website Hosting</h3>
    <p>We provide the fast and secure hosting for your website. We take care of all the maintenance so all you have to do is create content for your site. Best of all, you don't have to pay a cent for hosting for as long as your domain is registered with us.</p>
  </article>
  <article class="feature" style="left:123px;top:213px">
    <h3><svg width="18" height="18" viewBox="0 0 18 18"><circle cx="7" cy="7" r="5.5" fill="none" stroke="#5ca82a" stroke-width="2.4"/><path d="M11 11l6 6" stroke="#5ca82a" stroke-width="3"/></svg>Free Search Engine Optimisation</h3>
    <p>What good is the best looking website if no one visits it? We thought about that too! All our sites are optimised for search engines by default to ensure that your website is found by Searchly and other search engines like Findr and Lookwise.<br>Free Business Class Support</p>
  </article>
  <article class="feature" style="left:402px;top:213px">
    <h3><svg width="26" height="18" viewBox="0 0 26 18"><path d="M4 15V10a9 9 0 0 1 18 0v5" fill="none" stroke="#5ca82a" stroke-width="2.4"/><rect x="2" y="11" width="4" height="7" fill="#5ca82a"/><rect x="20" y="11" width="4" height="7" fill="#5ca82a"/></svg>Free Business Class Support</h3>
    <p>This is a point of pride for us and we are here to help. We're available to you 24 hours a day, everyday. Many of our competitors don't even provide a phone number for you to call! You deserve the best, and we won't settle for providing anything less.</p>
  </article>
  <article class="feature" style="left:680px;top:213px">
    <h3><svg width="22" height="20" viewBox="0 0 22 20"><text x="4" y="17" font-family="Arimo,sans-serif" font-weight="700" font-size="19" fill="#5ca82a">$</text></svg>Guaranteed renewal price</h3>
    <p>You'll never pay more to renew your domain name than the rate you paid when you initially registered it, or what our registration rate was when you transferred. (The only exceptions would be if you took advantage of a limited-time, special price)</p>
  </article>
</section>

<footer class="site-footer">
  <div class="footer-col" style="left:118px;width:115px"><h4>DOMAINS</h4><ul><li>Register Domains</li><li>Transfer Domains</li><li>Renew Domains</li><li>Name Servers</li></ul></div>
  <div class="footer-col" style="left:250px;width:114px"><h4>CREATOR</h4><ul><li>Menu Item</li><li>Menu Item</li><li>Menu Item</li><li>Menu Item</li></ul></div>
  <div class="footer-col" style="left:378px;width:88px"><h4>EMAIL</h4><ul><li>Menu Item</li><li>Menu Item</li><li>Menu Item</li><li>Menu Item</li></ul></div>
  <div class="footer-col" style="left:484px;width:109px"><h4>HOSTING</h4><ul><li>Menu Item</li><li>Menu Item</li><li>Menu Item</li><li>Menu Item</li></ul></div>
  <div class="footer-col" style="left:608px;width:82px"><h4>MARKETING</h4><ul><li>Menu Item</li><li>Menu Item</li><li>Menu Item</li><li>Menu Item</li></ul></div>
  <div class="footer-contact">
    <div class="ask">HAVE A QUESTION FOR US?</div>
    <div class="big">CONTACT US</div>
    <div class="phone">1300 55 01 27</div>
  </div>
</footer>

</body>
</html>
```